Wine Lable

We Are Moralba Ridge Wines and we are designing a new bottle for our top end wine named "The Velvet Harvest" I no exactly how i want the label to look and im searching for a talented designer to out my vision to life.

There will be 3 parts to this design.

Top Cover design with gold text wrapped around saying"The Velvet Harvest" (See Fig 2)

The front label which i want same as attached (See fig 2)

The Rear label
(See Fig 2 for design)
(See Fig 3 for content)

and final bottle design how it will look together
Updates

Come on guys keep the designs coming

Project Deadline Extended
Reason: I have extended my deadline due to the break from work over the Christmas new year period. Extra consideration will be made

Target Market(s)

The High End wine consumers the bottle cost will be $100USD

Font styles to use
Decorative
Script

Requirements
Must have

• Top Cover design with gold text wrapped around saying"The Velvet Harvest" (See Fig 2)
Black Rear Label with information and company name (Layout Fig 2) (Content Fig 3)
Gold and Black theme
The Text "Wine of Australia" somewhere on the bottle

```html
<!DOCTYPE html>
<html lang="en">
<head>
<meta charset="utf-8">
<title>The Velvet Harvest – Label Set</title>
<link href="https://fonts.googleapis.com/css2?family=Great+Vibes&family=Montserrat:wght@400;500&display=swap" rel="stylesheet">
<style>
  :root{
    --paper:#ffffff;
    --ink:#2f2625;
    --gold-dark:#c18e1f;
    --gold-mid:#e0b441;
    --gold-light:#f6dc85;
    --gold-grad:linear-gradient(135deg,var(--gold-dark) 0%,var(--gold-light) 45%,var(--gold-mid) 70%,var(--gold-dark) 100%);
  }
  *{margin:0;padding:0;box-sizing:border-box}
  html,body{width:753px;height:1200px;overflow:hidden;background:var(--paper)}
  .canvas{position:relative;width:753px;height:1200px;background:var(--paper)}
  .script{font-family:"Great Vibes",cursive;font-weight:400}
  .sans{font-family:"Montserrat",sans-serif}

  /* Top cover */
  .cap{position:absolute;left:292px;top:65px;width:169px;height:190px;background:var(--ink)}
  .cap__band{position:absolute;left:0;bottom:0;width:100%;height:47px;background:var(--gold-grad);padding:6px 7px}
  .cap__plate{width:100%;height:100%;background:var(--ink);display:flex;align-items:center;justify-content:center;border:1px solid var(--gold-light);overflow:hidden}
  .cap__name{font-size:17px;word-spacing:2px;color:var(--gold-mid);white-space:nowrap}

  /* Front label */
  .front{position:absolute;left:211px;top:347px;width:331px;height:398px}
  .front__pattern{position:absolute;inset:0;background:var(--gold-grad)}
  .front__plate{position:absolute;left:22px;top:100px;width:284px;height:68px;background:var(--paper);display:flex;align-items:center;justify-content:center;box-shadow:0 0 0 3px var(--gold-light);overflow:hidden}
  .front__name{font-size:33px;word-spacing:4px;color:var(--gold-mid);white-space:nowrap;line-height:1}

  /* Rear label */
  .rear{position:absolute;left:295px;top:815px;width:163px;height:320px;background:var(--ink)}
  .rear__frame{position:absolute;inset:5px;border:1px solid var(--gold-mid)}
  .rear__header{position:absolute;left:9px;top:15px;width:145px;height:47px;background:var(--gold-grad);padding:6px}
  .rear__header-plate{width:100%;height:100%;background:var(--ink);display:flex;align-items:center;justify-content:center;overflow:hidden}
  .rear__header-name{font-size:15px;word-spacing:2px;color:var(--gold-mid);white-space:nowrap}
  .rear__estate{position:absolute;left:0;top:72px;width:100%;text-align:center;font-size:5.5px;color:var(--gold-mid);letter-spacing:.2px}
  .rear__notes{position:absolute;left:12px;top:82px;width:140px;font-size:5.3px;line-height:1.5;color:var(--gold-light)}
  .rear__map{position:absolute;left:34px;top:132px;width:92px;height:86px;background:var(--gold-grad);border-radius:40% 46% 38% 42%}
  .rear__facts{position:absolute;left:12px;top:225px;width:140px;display:flex;justify-content:space-between;font-size:5.3px;color:var(--gold-light)}
  .rear__std{position:absolute;left:0;top:238px;width:100%;text-align:center;font-size:4.6px;line-height:1.5;color:var(--gold-light)}
  .rear__producer{position:absolute;left:48px;top:254px;width:66px;border:1px solid var(--gold-mid);padding:3px 2px;font-size:4.3px;line-height:1.45;color:var(--gold-light);text-align:center;text-transform:uppercase}
</style>
</head>
<body>
<main class="canvas">

  <section class="cap" aria-label="Top cover">
    <div class="cap__band">
      <div class="cap__plate"><span class="cap__name script">The Velvet Harvest</span></div>
    </div>
  </section>

  <section class="front" aria-label="Front label">
    <div class="front__pattern" role="img" aria-label="Gold labyrinth pattern filling the front label"></div>
    <div class="front__plate"><h1 class="front__name script">The Velvet Harvest</h1></div>
  </section>

  <section class="rear sans" aria-label="Rear label">
    <div class="rear__frame"></div>
    <div class="rear__header">
      <div class="rear__header-plate"><span class="rear__header-name script">The Velvet Harvest</span></div>
    </div>
    <p class="rear__estate">MORALBA RIDGE WINES</p>
    <p class="rear__notes">Deep, vibrant crimson/garnet colour. Blackcurrant and plum aromas with lifted, clove-like spice complemented by toasty oak and a touch of fennel. Intense but balanced juicy red currant and plum characters on the palate with a gentle spice. Generous, soft mouth-filling tannins and balanced acidity.</p>
    <div class="rear__map" role="img" aria-label="Gold map of Australia with the wine region highlighted"></div>
    <div class="rear__facts"><span>NET CONTENT 750ML</span><span>ALCOHOL STRENGTH 15.5%</span></div>
    <p class="rear__std">APPROX. 9.1 STANDARD DRINKS<br>CONTAINS SULPHITES</p>
    <p class="rear__producer">Produced by: Kestrel Vale Cellars<br>Unit 4, 112 Harrow Lane<br>Glenmore 5099<br>South Australia, Australia</p>
  </section>

</main>
</body>
</html>
```